Cybersecurity Start-Up - Korvelo

We need a power-point design for a new company based in Madrid (Spain) called 'Korvelo'. We aim to provide cybersecurity services to small- medium size companies for whom security is critical but paying big money to huge companies is not affordable.

The final design should communicate several things. As technology company which provides cybersecurity, it should be seen as something modern and futuristic , combined with safety and protection.

The company name Korvelo comes from Numantia, an ancient Celtiberian settlement in Spain which is famous for its role in the Celtiberian Wars (130 BC). They fought with Rome for 20 years , while being numerical inferior. And they won several times. When a final siege ocurred after a massive deployment of Rome legions, they held their ground for more than a year without food. When the situation was not longer sustainable, they decided to commit suicide rather than become slaves.

So the vision to hold the ground no matter what, should be communicated too
Updates

Need extra days to review

Requirements
Must have
• Check files attached for the logo of the company

```html
<!DOCTYPE html>
<html lang="en">
<head>
<meta charset="utf-8">
<title>Korvelo – Services Slide</title>
<link rel="stylesheet" href="https://fonts.googleapis.com/css2?family=Titillium+Web:wght@400;600;700&display=swap">
<style>
  :root {
    --brand-orange: #d64a00;
    --header-red: #e2321c;
    --header-orange: #f05a1e;
    --footer-orange: #f7941d;
    --white: #ffffff;
    --text-light: #fff3ea;
  }
  * { margin: 0; padding: 0; box-sizing: border-box; }
  html, body {
    width: 1200px; height: 900px; overflow: hidden;
    background: var(--white);
    font-family: "Titillium Web", Arial, sans-serif;
  }
  .slide { position: relative; width: 1200px; height: 900px; background: var(--white); }

  .slide-header {
    position: absolute; left: 0; top: 0; width: 1200px; height: 95px;
    background: linear-gradient(90deg, var(--header-red) 0%, var(--header-red) 45%, var(--header-orange) 75%, #e5412a 100%);
  }
  .slide-title {
    position: absolute; left: 26px; top: 16px;
    color: var(--white); font-weight: 600; font-size: 44px; line-height: 60px;
  }
  .brand-name {
    position: absolute; right: 70px; top: 20px;
    color: var(--white); font-weight: 600; font-size: 40px; line-height: 52px;
  }

  .slide-body {
    position: absolute; left: 0; top: 108px; width: 1200px; height: 747px;
    background: var(--brand-orange);
  }
  .service {
    position: absolute; top: 162px; width: 300px; text-align: center; color: var(--white);
  }
  .service--security { left: 75px; }
  .service--support { left: 458px; }
  .service--network { left: 842px; }
  .service-icon {
    display: block; width: 90px; height: 90px; margin: 0 auto;
    border-radius: 50%; background: var(--white);
  }
  .service-icon svg { display: block; width: 90px; height: 90px; }
  .service-title {
    margin-top: 33px; font-weight: 400; font-size: 26px; line-height: 30px;
    letter-spacing: 2.4px; text-transform: uppercase;
  }
  .service-text {
    margin-top: 30px; font-size: 20px; line-height: 31.5px; color: var(--text-light);
  }

  .slide-footer {
    position: absolute; left: 0; top: 867px; width: 1200px; height: 33px;
    background: var(--footer-orange);
  }
  .copyright {
    position: absolute; left: 10px; top: 4px;
    color: var(--white); font-size: 19px; line-height: 26px;
  }
</style>
</head>
<body>
<main class="slide">
  <header class="slide-header" role="img" aria-label="Header photo of glowing programming code on a red background">
    <h1 class="slide-title">Project Title Here</h1>
    <div class="brand-name">Korvelo</div>
  </header>

  <section class="slide-body">
    <article class="service service--security">
      <span class="service-icon">
        <svg viewBox="0 0 90 90" aria-hidden="true">
          <circle cx="45" cy="45" r="11" fill="none" stroke="#d64a00" stroke-width="3"/>
          <path d="M37 39c3 0 5 2 4 5s2 4 1 7M48 35c-1 3 2 4 4 4s3 3 1 5-1 5 1 6" fill="none" stroke="#d64a00" stroke-width="3"/>
        </svg>
      </span>
      <h2 class="service-title">Security<br>Development</h2>
      <p class="service-text">Toffee caramels candy canes bonbon bonbon soufflé bonbon wafer. Topping I love halvah I love. Jujubes lemon drops I love jelly pie chocolate bar. Biscuit oat cake carrot cake. Muffin jelly beans chocolate chocolate. Sugar plum I love cheesecake marshmallow oreo cake sweet cookies topping jelly gummies.</p>
    </article>

    <article class="service service--support">
      <span class="service-icon">
        <svg viewBox="0 0 90 90" aria-hidden="true">
          <g fill="#d64a00">
            <circle cx="42" cy="43" r="6"/>
            <rect x="40" y="33" width="4" height="20"/>
            <rect x="32" y="41" width="20" height="4"/>
            <rect x="40" y="33" width="4" height="20" transform="rotate(45 42 43)"/>
            <rect x="40" y="33" width="4" height="20" transform="rotate(-45 42 43)"/>
            <circle cx="52" cy="52" r="3.5"/>
          </g>
          <circle cx="42" cy="43" r="2.5" fill="#fff"/>
        </svg>
      </span>
      <h2 class="service-title">Technical<br>Support</h2>
      <p class="service-text">Toffee caramels candy canes bonbon bonbon soufflé bonbon wafer. Topping I love halvah I love. Jujubes lemon drops I love jelly pie chocolate bar. Biscuit oat cake carrot cake. Muffin jelly beans chocolate chocolate. Sugar plum I love cheesecake marshmallow oreo cake sweet cookies topping jelly gummies.</p>
    </article>

    <article class="service service--network">
      <span class="service-icon">
        <svg viewBox="0 0 90 90" aria-hidden="true">
          <path d="M45 32a9 9 0 0 0-5 16.5V52h10v-3.5A9 9 0 0 0 45 32z" fill="#d64a00"/>
          <rect x="40" y="54" width="10" height="2.5" fill="#d64a00"/>
          <rect x="41.5" y="58" width="7" height="2.5" fill="#d64a00"/>
        </svg>
      </span>
      <h2 class="service-title">Network<br>Solutions</h2>
      <p class="service-text">Toffee caramels candy canes bonbon bonbon soufflé bonbon wafer. Topping I love halvah I love. Jujubes lemon drops I love jelly pie chocolate bar. Biscuit oat cake carrot cake. Muffin jelly beans chocolate chocolate. Sugar plum I love cheesecake marshmallow oreo cake sweet cookies topping jelly gummies.</p>
    </article>
  </section>

  <footer class="slide-footer">
    <p class="copyright">Copyright text here</p>
  </footer>
</main>
</body>
</html>
```